New company website for Redfern Hollow Builders

We're looking to build a new company website that customers can use to contact us, get quotes, view past projects (renovations, additions, new construction, etc.), & learn more about our business. We want to use WordPress for our website and have already purchased the Lumo theme (by Parcel Layouts). Using that theme isn't required but we already have several examples of websites that we want to model our site after that use this theme. The "look" we're after is simple, light, & clean.

Target Market(s)

Residential remodeling, renovations, and new construction.

Industry/Entity Type

Residential Construction

Coding

Coded - Design and coding required

Number of Pages Required

5+ page

Font styles to use
Sans Serif

Colors
33a6d7
aaaaaa

Requirements
Must have
• We require the website to be coded using the Lumo theme. We'll be upgrading the project to include this today or tomorrow.
• The navigation bar should be static & remain at the top of the page. When scrolling we'd like the logo & info in the nav bar to size down. Here's an example of a site that does this: https://qrvhomesite.example/
Nice to have
• In the gallery with pictures of our finished product/jobs, when you mouse over the image, we'd like there to be additional info that shows up. For example, look at this gallery: https://qrvhomesite.example/projectcategories/kitchens/ We'll add a name/location of the job like: "Brandt kitchen - Apex, N.C."
• If you go to this website: https://lornbuildworks.example/ and scroll down to the pictures, we like how the picture moves and is interactive.

```html
<!DOCTYPE html>
<html lang="en">
<head>
<meta charset="utf-8">
<title>Redfern Hollow Builders</title>
<link href="https://fonts.googleapis.com/css2?family=Exo+2:wght@300;400;500&family=Montserrat:wght@400;500;600;700&family=Lora:ital@1&display=swap" rel="stylesheet">
<style>
:root{
  --blue:#33a6d7;
  --blue-dark:#2a8fbb;
  --navy:#17384f;
  --grey:#aaaaaa;
  --text:#555a5f;
  --heading:#5e6266;
  --light:#f4f5f6;
  --white:#ffffff;
  --footer:#efefef;
}
*{box-sizing:border-box;margin:0;padding:0}
html,body{width:1200px;height:3774px;overflow:hidden}
body{position:relative;background:var(--white);font-family:"Montserrat",sans-serif;color:var(--text)}
.abs{position:absolute}
.display{font-family:"Exo 2",sans-serif;font-weight:400;letter-spacing:2px;text-transform:uppercase}

/* header */
.site-header{left:0;top:0;width:1200px;height:90px;background:var(--white);box-shadow:0 1px 4px rgba(0,0,0,.08);z-index:5}
.brand{left:36px;top:28px;font-family:"Exo 2",sans-serif;font-weight:500;font-size:19px;color:var(--heading);letter-spacing:2px;text-transform:uppercase;display:flex;align-items:center;gap:9px}
.brand-mark{width:14px;height:14px;background:var(--blue)}
.nav{left:330px;top:37px;display:flex;gap:14px;font-size:11px;color:#666;white-space:nowrap}
.nav span::after{content:" \25BE";font-size:9px;color:var(--grey)}
.nav-phone{left:790px;top:37px;font-size:11px;font-weight:700;color:var(--blue);white-space:nowrap}
.btn-outline-header{left:928px;top:30px;width:242px;height:36px;border:2px solid var(--blue);color:var(--blue);font-size:12px;font-weight:700;text-transform:uppercase;display:flex;align-items:center;justify-content:center;letter-spacing:.5px}

/* hero */
.hero-photo{left:0;top:90px;width:1200px;height:510px;background:linear-gradient(100deg,#8a7763 0%,#c9b59b 35%,#e4dbcd 60%,#9e9384 100%)}
.hero-title{left:118px;top:205px;font-size:50px;line-height:62px;color:var(--white)}
.hero-copy{left:118px;top:337px;width:520px;font-size:16px;line-height:24px;color:var(--white)}
.btn{height:40px;display:flex;align-items:center;justify-content:center;gap:8px;font-size:13px;font-weight:600}
.btn-learn{left:118px;top:420px;width:152px;background:var(--white);color:#444}
.btn-process{left:283px;top:420px;width:132px;background:var(--blue);color:var(--white)}
.dots{display:flex;gap:6px}
.dots i{width:9px;height:9px;border-radius:50%;border:1px solid var(--grey);background:var(--white)}
.dots i.on{background:var(--grey)}
.hero-dots{left:578px;top:523px}
.hero-dots i{border-color:var(--white);background:transparent}
.hero-dots i.on{background:var(--white)}

/* planning form */
.plan-form{left:845px;top:138px;width:292px;height:767px;background:var(--blue);z-index:4;box-shadow:0 4px 14px rgba(0,0,0,.2)}
.plan-head{height:102px;background:var(--navy);color:var(--white);font-weight:700;font-size:20px;line-height:26px;text-align:center;padding-top:24px;text-transform:uppercase}
.field{position:absolute;left:18px;width:257px;height:31px;border:1px solid rgba(255,255,255,.55);background:rgba(255,255,255,.08);color:var(--white);font-size:10px;padding:9px 8px;white-space:nowrap;overflow:hidden}
.field.select{padding-right:32px}
.field.select::after{content:"\25BE";position:absolute;right:0;top:0;width:26px;height:29px;background:var(--navy);color:var(--white);text-align:center;line-height:29px;font-size:11px}
.field.area{height:101px}
.check{left:18px;top:655px;display:flex;gap:10px;align-items:center;color:var(--white);font-size:10px}
.check i{width:13px;height:13px;border:1px solid var(--white)}
.submit{left:18px;top:687px;width:257px;height:48px;background:var(--white);color:var(--blue);font-weight:600;font-size:18px;letter-spacing:2px;display:flex;align-items:center;justify-content:center}
.close{left:1163px;top:133px;width:34px;height:34px;border-radius:50%;background:var(--blue);color:var(--white);font-size:18px;display:flex;align-items:center;justify-content:center;z-index:4}

/* features */
.features{left:0;top:600px;width:845px;height:150px;background:var(--white);border-bottom:1px solid #eee}
.feature{top:0;height:150px;display:flex;align-items:center;justify-content:center;gap:14px;font-size:15px;text-transform:uppercase;color:#666}
.feature-trust{left:0;width:395px}
.feature-comm{left:395px;width:410px;color:var(--blue);box-shadow:0 0 14px rgba(0,0,0,.1);border-bottom:4px solid var(--blue)}

/* portfolio */
.portfolio-bg{left:0;top:752px;width:1200px;height:910px;background:linear-gradient(180deg,#f1f2f3,#fafafa 40%,#fff)}
.portfolio-line{left:0;top:752px}
.portfolio-title{left:118px;top:940px;font-size:34px;line-height:46px;color:var(--heading)}
.portfolio-title b{font-weight:500;color:var(--blue)}
.portfolio-copy{left:118px;top:1043px;width:380px;font-size:13px;line-height:20px;color:var(--grey)}
.btn-small{left:118px;top:1125px;width:100px;height:32px;border:1px solid #999;font-size:11px;color:#555;display:flex;align-items:center;justify-content:center;background:var(--white)}
.tile{width:536px;height:388px}
.tile-caption{position:absolute;left:36px;bottom:34px;width:440px;color:var(--white);font-size:13px;line-height:18px}
.tile-caption strong{display:block;font-size:15px;text-transform:uppercase;margin-bottom:8px}
.tile-kitchen{left:601px;top:875px;background:linear-gradient(160deg,#cfcac1,#8d877d 55%,#3b3732)}
.tile-spaces{left:63px;top:1265px;background:linear-gradient(170deg,#f2efe9,#cfc6b6 55%,#7b5e43)}
.tile-bath{left:601px;top:1265px;background:linear-gradient(150deg,#e9e4da,#b8ad9b 55%,#6a5d4d)}

/* testimonials */
.testimonials-bg{left:0;top:1794px;width:1200px;height:848px;background:linear-gradient(180deg,#eceef0,#e2e3e3 50%,#d8d6d2)}
.section-title{width:1200px;left:0;text-align:center;font-size:34px;color:var(--heading)}
.section-title b{font-weight:400;color:var(--blue)}
.section-sub{width:1200px;left:0;text-align:center;font-size:13px;color:#777}
.card{width:265px;height:322px;background:var(--white);text-align:center;padding-top:98px;box-shadow:0 2px 8px rgba(0,0,0,.06)}
.card.featured{width:325px;height:349px;background:var(--blue);padding-top:108px}
.card h3{font-weight:400;font-size:16px;color:var(--blue)}
.card .role{font-size:10px;color:#777;margin-top:8px}
.card p{font-family:"Lora",serif;font-style:italic;font-size:11px;line-height:17px;color:#888;width:200px;margin:18px auto 0}
.card.featured h3,.card.featured .role,.card.featured p{color:var(--white)}
.card .quote{font-family:"Lora",serif;font-size:30px;color:#555;margin-top:12px;font-style:normal}
.card.featured .quote{color:var(--white)}
.avatar{width:164px;height:164px;border-radius:50%;border:6px solid var(--white);background:linear-gradient(180deg,#d5d5d5,#8a8a8a);z-index:2}
.test-dots{left:576px;top:2532px}

/* before after */
.ba-img{top:2840px;width:343px;height:250px}
.ba-before{left:247px;background:linear-gradient(160deg,#d9c6a8,#9b6b3d 55%,#5c3b1f)}
.ba-after{left:606px;background:linear-gradient(160deg,#eceae4,#b9b5aa 55%,#4a4845)}
.ba-label{position:absolute;left:12px;bottom:8px;color:var(--white);font-size:15px;text-transform:uppercase;letter-spacing:1px}
.ba-img.ba-after .ba-label{left:auto;right:14px}
.arrow{top:2948px}
.ba-dots{left:578px;top:3145px}

/* cta */
.cta{left:0;top:3236px;width:1200px;height:181px;background:linear-gradient(90deg,#4e5154,#6c6e70 50%,#4a4c4e)}
.cta-box{left:282px;top:3285px;width:634px;height:74px;border-top:1px solid rgba(255,255,255,.7);border-bottom:1px solid rgba(255,255,255,.7);display:flex;align-items:center;justify-content:center;color:var(--white);font-size:33px}

/* footer */
.site-footer{left:0;top:3417px;width:1200px;height:302px;background:var(--footer)}
.fcol{top:3490px;font-size:11px;line-height:18px;color:#666}
.fcol h4{font-size:11px;font-weight:700;color:#444;margin-bottom:12px}
.footer-brand{left:0;width:1200px;top:3655px;display:flex;justify-content:center;align-items:center;gap:9px;font-family:"Exo 2",sans-serif;font-weight:500;font-size:16px;color:#777;letter-spacing:2px;text-transform:uppercase}
.footer-brand i{width:11px;height:11px;background:#777}
.bottom-bar{left:0;top:3719px;width:1200px;height:55px;background:var(--blue);color:var(--white);font-size:11px}
.copyright{left:118px;top:20px}
.social{left:860px;top:20px;font-weight:700}
.social-dots{left:990px;top:13px;display:flex;gap:8px}
.social-dots i{width:27px;height:27px;border-radius:50%;border:1.5px solid var(--white)}
</style>
</head>
<body>

<header class="site-header abs">
  <div class="brand abs"><i class="brand-mark"></i>Redfern Hollow</div>
  <nav class="nav abs"><span>Getting Started</span><span>Who We Are</span><span>Specialties</span><span>Portfolio</span><span>Contact Us</span></nav>
  <div class="nav-phone abs">Call: (555) 014 2290</div>
  <div class="btn-outline-header abs">Start Planning Your Project</div>
</header>

<section class="hero">
  <div class="hero-photo abs" role="img" aria-label="Photo of a luxury bathroom with solid surface vanity and tiled backsplash"></div>
  <h1 class="hero-title display abs">Solid Surface<br>Luxury Bathroom</h1>
  <p class="hero-copy abs">Lorem ipsum dolor sit amet, consectetur adipiscing elit, sed do eiusmod tempor incididunt ut labore</p>
  <div class="btn btn-learn abs">Learn More
    <svg width="14" height="14" viewBox="0 0 14 14"><circle cx="7" cy="7" r="7" fill="#444"/><path d="M5 4l3 3-3 3" stroke="#fff" stroke-width="1.6" fill="none"/></svg></div>
  <div class="btn btn-process abs">Our Process
    <svg width="14" height="14" viewBox="0 0 14 14"><circle cx="7" cy="7" r="7" fill="#fff"/><path d="M5 4l3 3-3 3" stroke="#33a6d7" stroke-width="1.6" fill="none"/></svg></div>
  <div class="dots hero-dots abs"><i class="on"></i><i></i><i></i></div>
</section>

<aside class="plan-form abs">
  <div class="plan-head">Start Planning<br>Your Project</div>
  <div class="field" style="top:114px">First &amp; Last Name</div>
  <div class="field" style="top:152px">Phone Number</div>
  <div class="field" style="top:190px">Email</div>
  <div class="field" style="top:228px">Project Address</div>
  <div class="field" style="top:266px">Project Zip Code</div>
  <div class="field select" style="top:304px">Project Type</div>
  <div class="field select" style="top:342px">Do you have a vision for your project?</div>
  <div class="field select" style="top:380px">Have you remodeled before?</div>
  <div class="field select" style="top:418px">How did you hear about us?</div>
  <div class="field" style="top:456px">Person who referred me</div>
  <div class="field" style="top:494px">Best Weekday &amp; Time to Reach You</div>
  <div class="field area" style="top:532px">Questions or Message for Team Redfern</div>
  <div class="check abs"><i></i>Add me to your list for design inspiration!</div>
  <div class="submit abs">SUBMIT</div>
</aside>
<div class="close abs">&times;</div>

<section class="features abs">
  <div class="feature feature-trust abs">
    <svg width="24" height="24" viewBox="0 0 24 24" fill="none" stroke="#666" stroke-width="1.6"><circle cx="12" cy="10" r="6"/><path d="M8 15l-2 7 6-3 6 3-2-7"/></svg>
    Proven Trust</div>
  <div class="feature feature-comm abs">
    <svg width="26" height="20" viewBox="0 0 26 20" fill="none" stroke="#33a6d7" stroke-width="1.8"><rect x="1" y="1" width="24" height="18"/><path d="M1 1l12 10L25 1"/></svg>
    Constant Communication</div>
</section>

<section class="portfolio">
  <div class="portfolio-bg abs"></div>
  <svg class="portfolio-line abs" width="1200" height="520" viewBox="0 0 1200 520"><path d="M770 0L380 510" stroke="#dddddd" stroke-width="1.5"/></svg>
  <h2 class="portfolio-title display abs">Redfern Hollow<br><b>Portfolio</b></h2>
  <p class="portfolio-copy abs">Lorem ipsum dolor sit amet, consectetur adipiscing, sed do eiusmod tempor incididunt ut labore et dolore magna aliqua.</p>
  <div class="btn-small abs">Learn More</div>
  <div class="tile tile-kitchen abs" role="img" aria-label="Photo of a renovated kitchen with white cabinets and stone backsplash">
    <div class="tile-caption"><strong>Kitchen</strong>Lorem ipsum dolor sit amet, consectetur adipiscing elit, sed do eiusmod tempor.</div></div>
  <div class="tile tile-spaces abs" role="img" aria-label="Photo of a new open living space with wood floors and stone fireplace">
    <div class="tile-caption"><strong>New Spaces</strong>Lorem ipsum dolor sit amet, consectetur adipiscing elit, sed do eiusmod tempor.</div></div>
  <div class="tile tile-bath abs" role="img" aria-label="Photo of a bathroom with freestanding tub and glass shower">
    <div class="tile-caption"><strong>Bathroom</strong>Lorem ipsum dolor sit amet, consectetur adipiscing elit, sed do eiusmod tempor.</div></div>
</section>

<section class="testimonials">
  <div class="testimonials-bg abs" role="img" aria-label="Faded photo of a bright white kitchen interior"></div>
  <h2 class="section-title display abs" style="top:1920px">Client <b>Testimonials</b></h2>
  <p class="section-sub abs" style="top:1980px">Redfern Hollow Builders what says our clients</p>

  <div class="avatar abs" style="left:208px;top:2068px" role="img" aria-label="Portrait photo of Caleb Ainsworth"></div>
  <div class="card abs" style="left:158px;top:2151px">
    <h3>Caleb Ainsworth</h3><div class="role">Bathroom Project</div>
    <p>Founder Caleb Ainsworth divides his time between directing sales and managing projects from a hands-on approach, having been in the field</p>
    <div class="quote">&rdquo;</div></div>

  <div class="card featured abs" style="left:445px;top:2141px">
    <h3>Marcus Delacroix</h3><div class="role">Kitchen Project</div>
    <p>Marcus manages every floor and tile project, from scheduling crews to final touches on all remodeling jobs. Having grown up on a sawmill and helping build houses, he has</p>
    <div class="quote">&rdquo;</div></div>
  <div class="avatar abs" style="left:526px;top:2040px" role="img" aria-label="Portrait photo of Marcus Delacroix"></div>

  <div class="avatar abs" style="left:843px;top:2068px" role="img" aria-label="Portrait photo of Owen Petrakis"></div>
  <div class="card abs" style="left:793px;top:2151px">
    <h3>Owen Petrakis</h3><div class="role">Kitchen Project</div>
    <p>A local native and state graduate with a BS in Business Management, Owen has been intrigued with how things are built since</p>
    <div class="quote">&rdquo;</div></div>

  <div class="dots test-dots abs"><i></i><i class="on"></i><i></i><i></i></div>
</section>

<section class="before-after">
  <h2 class="section-title display abs" style="top:2728px">Before <b>And</b> After</h2>
  <p class="section-sub abs" style="top:2787px">Redfern Hollow Builders Before and After</p>
  <div class="ba-img ba-before abs" role="img" aria-label="Photo of a dated kitchen with oak cabinets before remodeling"><span class="ba-label">Before</span></div>
  <div class="ba-img ba-after abs" role="img" aria-label="Photo of the same kitchen after remodeling with white cabinets and granite"><span class="ba-label">After</span></div>
  <svg class="arrow abs" style="left:212px" width="14" height="24" viewBox="0 0 14 24"><path d="M12 2L3 12l9 10" stroke="#bbbbbb" stroke-width="2" fill="none"/></svg>
  <svg class="arrow abs" style="left:975px" width="14" height="24" viewBox="0 0 14 24"><path d="M2 2l9 10-9 10" stroke="#bbbbbb" stroke-width="2" fill="none"/></svg>
  <div class="dots ba-dots abs"><i></i><i class="on"></i><i></i><i></i></div>
</section>

<section class="cta abs" role="img" aria-label="Dark faded photo of architectural plans on a desk"></section>
<div class="cta-box display abs">Start Planning Your Project</div>

<footer class="site-footer abs"></footer>
<div class="fcol abs" style="left:118px"><h4>Getting Started</h4>Our Process<br>What to Expect<br>FAQs</div>
<div class="fcol abs" style="left:264px"><h4>Who We Are</h4>Our story<br>Redfern Team<br>Testimonials</div>
<div class="fcol abs" style="left:415px"><h4>Specialties</h4>Remodeling<br>New Home Construction<br>Additions</div>
<div class="fcol abs" style="left:616px"><h4>Portfolio</h4>Before and after<br>Kitchens<br>Bathrooms<br>Whole house</div>
<div class="fcol abs" style="left:772px"><h4>Contact Us</h4>Contact from<br>Link to CrewLedger</div>
<div class="fcol abs" style="left:928px"><h4>Contact Us</h4>
  <div style="display:flex;gap:10px"><svg width="14" height="12" viewBox="0 0 14 12"><rect x="1" y="1" width="12" height="10" fill="#888"/><path d="M1 1l6 5 6-5" stroke="#fff" fill="none"/></svg><span>Address<br>41 N. Linden Street,<br>Suite B, Hollis, N.C. 27000</span></div>
  <div style="display:flex;gap:10px;margin-top:10px"><svg width="14" height="14" viewBox="0 0 14 14"><path d="M3 1l3 3-2 2c1 2 2 3 4 4l2-2 3 3-2 2C6 13 1 8 1 3z" fill="#888"/></svg><span>555.014.2290</span></div>
</div>
<div class="footer-brand abs"><i></i>Redfern Hollow</div>

<div class="bottom-bar abs">
  <div class="copyright abs">&copy; 2018 &nbsp;Redfern Hollow Builders - Legal &amp; Privacy</div>
  <div class="social abs">Social Activity</div>
  <div class="social-dots abs"><i></i><i></i><i></i><i></i></div>
</div>

</body>
</html>
```